Interior Design & consultancy firm requires a new business card design that is a little bit funky bu

Meridale Design Services is a leading strategic design practice specialising in the development and implementation of strategies and design solutions for commercial workplaces across a wide variety of industries.

The company has over twenty years experience in the strategic design, development and construction of innovative and efficient workplace environments for the commercial, corporate and industrial sectors.

We believe good design and efficient workspaces can transform companies, improve people’s lives and increase productivity.

Target Market(s)

My clients are mainly Government or corporate clients wanting to create a statement with their office fitout & new furniture that reflects their corporate identity

Industry/Entity Type

Construction

Font styles to use
Sans Serif

Colors
add136

Requirements
Must have
• The business card must be easy to read, simple & highlight my name & mobile phone number
Should not have
• I do not want the card to be fussy, feature too many colours or look to busy.

```html
<!DOCTYPE html>
<html lang="en">
<head>
<meta charset="utf-8">
<title>Meridale Design Services – Business Card</title>
<link rel="stylesheet" href="https://fonts.googleapis.com/css2?family=Comfortaa:wght@700&family=Open+Sans:wght@300;400&display=swap">
<style>
  :root {
    --lime: #add136;
    --lime-deep: #8fb827;
    --lime-light: #c6e260;
    --ink: #3c3c3c;
    --ink-soft: #6a6a6a;
    --paper: #ffffff;
    --paper-shade: #f1f1f1;
    --backdrop: #e7e5e0;
  }
  * { box-sizing: border-box; margin: 0; padding: 0; }
  html, body {
    width: 1200px; height: 1024px; overflow: hidden;
    background: var(--backdrop);
    font-family: "Open Sans", sans-serif;
  }
  .canvas {
    width: 1200px; height: 1024px;
    display: flex; flex-direction: column; align-items: center; justify-content: center;
    gap: 40px;
  }
  .card {
    width: 770px; height: 440px;
    border-radius: 4px;
    box-shadow: 0 10px 30px rgba(0,0,0,0.15);
    position: relative; overflow: hidden;
  }
  .card-front {
    background: linear-gradient(135deg, var(--paper) 0%, var(--paper-shade) 100%);
    display: flex;
  }
  .card-front .edge-tab {
    position: absolute; top: 0; right: 70px;
    width: 28px; height: 10px; background: var(--lime);
  }
  .front-half {
    flex: 1; display: flex; flex-direction: column; justify-content: center;
    padding: 0 50px;
  }
  .divider {
    width: 1px; margin: 80px 0; background: var(--lime-light);
  }
  .brand { display: flex; align-items: center; gap: 14px; }
  .brand-square {
    width: 46px; height: 46px; border-radius: 8px; background: var(--lime);
  }
  .brand-name {
    font-family: "Comfortaa", sans-serif; font-weight: 700;
    font-size: 40px; color: var(--lime); letter-spacing: 0.5px;
  }
  .brand-sub {
    margin-top: 6px; margin-left: 60px;
    font-size: 15px; font-weight: 400; color: var(--ink-soft);
  }
  .address {
    margin-top: 30px; display: flex; align-items: center; gap: 8px;
    font-size: 14px; color: var(--ink); font-weight: 400;
  }
  .holder-name {
    font-family: "Comfortaa", sans-serif; font-weight: 700;
    font-size: 26px; color: var(--lime);
  }
  .holder-title {
    margin-top: 6px; font-size: 14px; font-weight: 300; color: var(--ink-soft);
  }
  .contacts { margin-top: 26px; display: flex; flex-direction: column; gap: 10px; }
  .contact-row { display: flex; align-items: center; gap: 8px; font-size: 15px; color: var(--ink); }
  .contact-row + .contact-row { margin-top: 0; }
  .phone-pair { display: flex; gap: 22px; }
  .phone-item { display: flex; align-items: center; gap: 8px; }
  .icon { width: 14px; height: 14px; flex: none; }
  .card-back {
    background: linear-gradient(135deg, var(--lime-light) 0%, var(--lime) 55%, var(--lime-deep) 100%);
  }
</style>
</head>
<body>
<main class="canvas">
  <section class="card card-front" aria-label="Business card front">
    <span class="edge-tab"></span>
    <div class="front-half front-company">
      <div class="brand">
        <span class="brand-square"></span>
        <span class="brand-name">Meridale</span>
      </div>
      <p class="brand-sub">Design Services Pty Ltd</p>
      <p class="address">
        <svg class="icon" viewBox="0 0 14 14"><path d="M7 1a4 4 0 0 0-4 4c0 3 4 8 4 8s4-5 4-8a4 4 0 0 0-4-4zm0 5.5A1.5 1.5 0 1 1 7 3.5a1.5 1.5 0 0 1 0 3z" fill="var(--lime)"/></svg>
        Address 1, Street, Place, ZIP
      </p>
    </div>
    <div class="divider"></div>
    <div class="front-half front-person">
      <h1 class="holder-name">Nadia Whitfield</h1>
      <p class="holder-title">Director &amp; Senior Interior Designer</p>
      <div class="contacts">
        <div class="contact-row phone-pair">
          <span class="phone-item">
            <svg class="icon" viewBox="0 0 14 14"><rect x="3.5" y="1" width="7" height="12" rx="1.2" fill="none" stroke="var(--lime)" stroke-width="1.3"/><circle cx="7" cy="11" r="0.7" fill="var(--lime)"/></svg>
            0491 570 156
          </span>
          <span class="phone-item">
            <svg class="icon" viewBox="0 0 14 14"><path d="M3 1.5l2 .3 1 3-1.4 1a7 7 0 0 0 3.6 3.6l1-1.4 3 1 .3 2c-.2 1-1 1.5-2 1.5C5.5 12.5 1.5 8.5 1.5 3.5c0-1 .5-1.8 1.5-2z" fill="var(--lime)"/></svg>
            04XXXXXXX
          </span>
        </div>
        <div class="contact-row">
          <svg class="icon" viewBox="0 0 14 14"><rect x="1" y="3" width="12" height="8.5" rx="1" fill="var(--lime)"/><path d="M1.5 3.5L7 8l5.5-4.5" fill="none" stroke="#fff" stroke-width="1.1"/></svg>
          nadia@meridale.com
        </div>
      </div>
    </div>
  </section>
  <section class="card card-back" role="img" aria-label="Business card back: lime green field with a faint large brand decoration"></section>
</main>
</body>
</html>
```